Hello Creative Minds!
Our business is after a elegant and classy flyer that draws attention!
The business is Velmora Turf - Lawn Rejuvenation Services. We provide services that maintain a healthy and vibrant green lawn through the tough Australian seasons. The products we use limits the water needed to keep grass green to a minimum - practically none at all! This not only helps the home owner or home seller but the environment by limiting the use of water that is needed to create a green lawn. The products we use are made from natural ingredients that are and pet friendly.
This fly will be our introductory offer to the market. Below are the required points that need to be on the flyer. Attached is the business logo, before & after pictures and 1 example of the LAYOUT not DESIGN of what the flyer should be laid out like or similar to. Feel free to use different 'Lawn Mower' pictures.
All the best; if you need any questions answered please feel free to message.
REQUIRED POINTS (Please re-phrase were possible);
*Instantly restores the natural green colour of grass – year round
*Lasts for up to 3 months
*Substantially reduces watering needs
*Pet friendly
*Stays green during droughts and water restrictions
*UV fade resistant
*Won’t bleed, run, or stain once absorbed into the grass
*Safe for the environment, pets and people
*Works in extreme heat, cold and frost
*Organic and natural – no harmful chemicals
*Reduces the amount of fertilizer
and water used on lawns
*Kerb appeal is essential for getting your property sold for the highest price possible
SERVICES & PRICING
Lawn maintenance (cut & trim) starting from $60
Lawn rejuvenation starting from $80 (Only $27 a month for 3 months)*
Package deal starting from $120
Introductory offer: 25% off all services. Refer a friend, when they book you receive another 25% off your next service.
LOCATIONS
Nowra to Sydney
CONTACT NUMBER
Will be posted with the winner - please leave an area for this.
SOCIAL MEDIA
Please add Chatterloop and Snapvista logo's
Updates
Competition has finished, thank you to all that have participated! I will review and comment on the flyers that need assistance. All the best with future designs!
Target Market(s)
home owners, home sellers, property developers, real estates and nursing homes and government housing.
Industry/Entity Type
Lawn Care
Look and feel
Each slider illustrates characteristics of the customer's brand and the style your logo design should communicate.

```html
<!DOCTYPE html>
<html lang="en">
<head>
<meta charset="utf-8">
<title>Velmora Turf - Lawn Rejuvenation Services</title>
<link href="https://fonts.googleapis.com/css2?family=Poppins:wght@400;500;600;700&family=Oswald:wght@500&display=swap" rel="stylesheet">
<style>
  :root {
    --page-bg: #ececec;
    --charcoal: #383b44;
    --green-deep: #15720f;
    --green-mid: #2c9a17;
    --green-light: #5cc22c;
    --green-head: #1d8a1a;
    --ink: #23252b;
    --white: #ffffff;
    --paper: #f4f4f4;
  }
  * { margin: 0; padding: 0; box-sizing: border-box; }
  html, body { width: 1113px; height: 1200px; overflow: hidden; background: var(--page-bg); }
  body { font-family: "Poppins", sans-serif; }

  .flyer {
    position: absolute; left: 143px; top: 20px;
    width: 826px; height: 1160px;
    background: var(--paper); overflow: hidden;
    box-shadow: 0 4px 14px rgba(0,0,0,.25);
  }
  .flyer-art { position: absolute; inset: 0; }

  .brand { position: absolute; left: 40px; top: 62px; color: var(--white); }
  .brand-name { font-size: 52px; font-weight: 500; line-height: 1; letter-spacing: .5px; }
  .brand-tag { font-size: 11px; letter-spacing: 4px; margin-top: 10px; padding-left: 40px; }

  .benefits { position: absolute; left: 37px; top: 238px; list-style: none; color: var(--white); }
  .benefits li { position: relative; padding-left: 24px; font-size: 17px; line-height: 27.3px; }
  .benefits li svg { position: absolute; left: 0; top: 8px; width: 13px; height: 11px; }

  .section-title {
    position: absolute; left: 0; width: 100%;
    display: flex; align-items: center; justify-content: center; gap: 10px;
    color: var(--green-head); font-weight: 600; font-size: 33px;
  }
  .section-title::before, .section-title::after {
    content: ""; width: 90px; height: 2px; background: var(--ink);
  }
  .title-services { top: 695px; }
  .title-offer { top: 855px; }

  .copy { position: absolute; left: 0; width: 100%; text-align: center; color: var(--ink); }
  .pricing { top: 742px; font-size: 21px; line-height: 31px; }
  .pricing .amount { font-size: 30px; font-weight: 700; }
  .offer { top: 910px; font-size: 24px; line-height: 32px; }
  .offer strong { font-weight: 700; }

  .footer {
    position: absolute; left: 0; bottom: 0; width: 100%; height: 72px;
    display: flex; align-items: center; padding: 0 22px; gap: 42px;
    color: var(--white); font-family: "Oswald", sans-serif; font-size: 26px; letter-spacing: .5px;
  }
  .socials { margin-left: auto; display: flex; flex-direction: column; font-family: "Poppins", sans-serif; font-size: 13px; font-weight: 500; line-height: 17px; letter-spacing: 0; }
</style>
</head>
<body>
<main class="flyer">
  <svg class="flyer-art" viewBox="0 0 826 1160" width="826" height="1160">
    <defs>
      <linearGradient id="lawnGrad" x1="0" y1="0" x2="0" y2="1">
        <stop offset="0" stop-color="#4fae2a"/>
        <stop offset=".5" stop-color="#2a9415"/>
        <stop offset="1" stop-color="#15720f"/>
      </linearGradient>
      <linearGradient id="footGrad" x1="0" y1="0" x2="0" y2="1">
        <stop offset="0" stop-color="#2c9a17"/>
        <stop offset="1" stop-color="#15720f"/>
      </linearGradient>
      <linearGradient id="turfGrad" x1="0" y1="0" x2="0" y2="1">
        <stop offset="0" stop-color="#f4f4f4"/>
        <stop offset="1" stop-color="#3aa81d"/>
      </linearGradient>
    </defs>
    <rect class="lawn-photo" x="0" y="0" width="826" height="700" fill="url(#lawnGrad)" role="img" aria-label="Photo of a freshly cut green lawn"/>
    <rect class="mower-photo" x="560" y="0" width="266" height="250" fill="#3f7a2a" opacity=".55" role="img" aria-label="Photo of a lawn mower on green grass"/>
    <path class="header-band" d="M0 0 H680 C560 70 420 190 220 195 C140 197 60 188 0 180 Z" fill="var(--charcoal)"/>
    <path d="M0 180 C60 188 140 197 220 195 C420 190 560 70 680 0" fill="none" stroke="#6fd13a" stroke-width="4"/>
    <path class="content-panel" d="M0 640 C200 560 470 650 826 500 V1160 H0 Z" fill="var(--paper)"/>
    <path d="M0 640 C200 560 470 650 826 500" fill="none" stroke="#1c7e12" stroke-width="4"/>
    <circle cx="702" cy="333" r="76" fill="#1c7e12"/>
    <circle cx="702" cy="333" r="70" fill="#a99a78" role="img" aria-label="Before and after photo of a dry lawn turned green"/>
    <circle cx="702" cy="501" r="76" fill="#1c7e12"/>
    <circle cx="702" cy="501" r="70" fill="#6f8a66" role="img" aria-label="Photo of a rejuvenated front lawn beside a fence"/>
    <rect x="0" y="1040" width="826" height="50" fill="url(#turfGrad)" role="img" aria-label="Border of grass blades"/>
    <rect x="0" y="1088" width="826" height="72" fill="url(#footGrad)"/>
  </svg>

  <header class="brand">
    <div class="brand-name">Velmora Turf</div>
    <div class="brand-tag">LAWN REJUVENATION SERVICES</div>
  </header>

  <ul class="benefits">
    <li><svg viewBox="0 0 13 11"><path d="M1 6 L5 10 L12 1" fill="none" stroke="#fff" stroke-width="2.2"/></svg>Instantly restores the natural green colour of grass – year round</li>
    <li><svg viewBox="0 0 13 11"><path d="M1 6 L5 10 L12 1" fill="none" stroke="#fff" stroke-width="2.2"/></svg>Lasts for up to 3 months</li>
    <li><svg viewBox="0 0 13 11"><path d="M1 6 L5 10 L12 1" fill="none" stroke="#fff" stroke-width="2.2"/></svg>Substantially reduces watering needs</li>
    <li><svg viewBox="0 0 13 11"><path d="M1 6 L5 10 L12 1" fill="none" stroke="#fff" stroke-width="2.2"/></svg>Pet friendly</li>
    <li><svg viewBox="0 0 13 11"><path d="M1 6 L5 10 L12 1" fill="none" stroke="#fff" stroke-width="2.2"/></svg>Stays green during droughts &amp; water restrictions</li>
    <li><svg viewBox="0 0 13 11"><path d="M1 6 L5 10 L12 1" fill="none" stroke="#fff" stroke-width="2.2"/></svg>UV fade resistant</li>
    <li><svg viewBox="0 0 13 11"><path d="M1 6 L5 10 L12 1" fill="none" stroke="#fff" stroke-width="2.2"/></svg>Won’t bleed, run, or stain once absorbed into the grass</li>
    <li><svg viewBox="0 0 13 11"><path d="M1 6 L5 10 L12 1" fill="none" stroke="#fff" stroke-width="2.2"/></svg>Safe for the environment, pets &amp; people</li>
    <li><svg viewBox="0 0 13 11"><path d="M1 6 L5 10 L12 1" fill="none" stroke="#fff" stroke-width="2.2"/></svg>Works in extreme heat, cold &amp; frost</li>
    <li><svg viewBox="0 0 13 11"><path d="M1 6 L5 10 L12 1" fill="none" stroke="#fff" stroke-width="2.2"/></svg>Organic &amp; natural – no harmful chemicals</li>
    <li><svg viewBox="0 0 13 11"><path d="M1 6 L5 10 L12 1" fill="none" stroke="#fff" stroke-width="2.2"/></svg>Reduces the amount of fertilizer &amp; water used on lawns</li>
    <li><svg viewBox="0 0 13 11"><path d="M1 6 L5 10 L12 1" fill="none" stroke="#fff" stroke-width="2.2"/></svg>Kerb appeal is essential for getting your property<br>sold for the highest price possible</li>
  </ul>

  <h2 class="section-title title-services">SERVICES &amp; PRICING</h2>
  <div class="copy pricing">
    <p>Lawn maintenance (cut &amp; trim) starting from <span class="amount">$60</span></p>
    <p>Lawn rejuvenation starting from <span class="amount">$80</span> (Only $27 a month for 3 months)*</p>
    <p>Package deal starting from <span class="amount">$120</span></p>
  </div>

  <h2 class="section-title title-offer">INTRODUCTORY OFFER</h2>
  <div class="copy offer">
    <p><strong>25% off</strong> all services.</p>
    <p>Refer a friend, when they book you receive another</p>
    <p><strong>25% off</strong> your next service.</p>
  </div>

  <footer class="footer">
    <span class="locations">LOCATIONS : NOWRA TO SYDNEY</span>
    <span class="phone">CALL US : 482-730-1596</span>
    <span class="socials"><span>Chatterloop</span><span>Snapvista</span></span>
  </footer>
</main>
</body>
</html>
```